Blue Harbor Trophies & Awards Unique Business Card Design

Recently selected a new logo design and waiting to recieve print files. I've attached image for your review. We are a trophies and awards company that provides engraving on trophies, plaques, name plates, name tags, desk sets, medals, acrylics, and signage.

We are located in Monroe, Louisiana and provide this service with computerized & laser engraving equipment.

Target Market(s)

Corporate, Sport, Church, and Special Events

Industry/Entity Type

Business

Contact Information for Business Card

I'd like to see the following list on the card: Trophies, Plaques, Name Plates, Name Tags, Desk Sets, Medals, Certificates... this is accomplished with Computerized & Laser Engraving

Colors
0555a3
ec1f27
ffffff

Requirements
Must have
• I like either single or double sided. If a design can be created with a frosted card stock I'd consider single. Must be Red, White, and Blue. Dale Penrow - Owner, 415 W 9th Ave, Millbrook, Ky 70384 office 555-555-2190 fax 555-555-2186 email: blueharbor@blueharbortrophyco.example, and website: www.blueharbortrophyco.example

```html
<!DOCTYPE html>
<html lang="en">
<head>
<meta charset="utf-8">
<title>Blue Harbor Trophies &amp; Awards – Business Card</title>
<link href="https://fonts.googleapis.com/css2?family=Open+Sans:wght@400;600;700;800&display=swap" rel="stylesheet">
<style>
  :root {
    --brand-blue: #0555a3;
    --brand-red: #ec1f27;
    --card-white: #ffffff;
    --ink: #1c1c1c;
    --backdrop: #e4e6ea;
  }
  * { margin: 0; padding: 0; box-sizing: border-box; }
  html, body { width: 1200px; height: 800px; overflow: hidden; }
  body {
    background: var(--backdrop);
    font-family: "Open Sans", Arial, sans-serif;
    position: relative;
  }
  .card {
    position: absolute;
    top: 246px;
    width: 540px;
    height: 309px;
    background: var(--card-white);
    box-shadow: 0 6px 18px rgba(0,0,0,.18);
    overflow: hidden;
  }
  .card--back { left: 40px; }
  .card--front { left: 620px; }
  .card__bands { position: absolute; inset: 0; width: 100%; height: 100%; }

  .wordmark {
    position: absolute;
    display: flex;
    align-items: center;
    gap: 10px;
    color: var(--brand-blue);
    font-weight: 700;
    line-height: 1.05;
  }
  .wordmark__dot {
    flex: none;
    border-radius: 50%;
    background: var(--brand-blue);
  }
  .wordmark__name { display: block; }

  /* contact side */
  .card--back .wordmark { left: 34px; top: 48px; }
  .card--back .wordmark__dot { width: 30px; height: 30px; }
  .card--back .wordmark__name--main { font-size: 21px; }
  .card--back .wordmark__name--sub { font-size: 15px; }

  .contact-list {
    position: absolute;
    left: 34px;
    top: 110px;
    list-style: none;
    font-size: 11.5px;
    color: var(--ink);
  }
  .contact-list__item {
    display: flex;
    align-items: center;
    gap: 8px;
    height: 21px;
  }
  .contact-list__icon { width: 13px; height: 13px; flex: none; }

  .owner {
    position: absolute;
    right: 40px;
    top: 196px;
    text-align: right;
  }
  .owner__name { font-size: 25px; font-weight: 800; color: var(--ink); letter-spacing: .2px; line-height: 1.1; }
  .owner__first { color: var(--brand-red); }
  .owner__title { font-size: 13px; font-weight: 700; color: var(--ink); margin-top: 2px; }

  /* product side */
  .card--front .wordmark { left: 118px; top: 70px; }
  .card--front .wordmark__dot { width: 40px; height: 40px; }
  .card--front .wordmark__name--main { font-size: 32px; }
  .card--front .wordmark__name--sub { font-size: 22px; }

  .products {
    position: absolute;
    left: 16px;
    right: 16px;
    top: 166px;
    color: var(--brand-blue);
    font-weight: 700;
  }
  .products__label { font-size: 12px; text-align: center; margin-bottom: 4px; }
  .products__list {
    list-style: none;
    display: flex;
    justify-content: center;
    flex-wrap: nowrap;
    font-size: 11.5px;
    white-space: nowrap;
  }
  .products__item + .products__item::before {
    content: "|";
    color: var(--brand-red);
    margin: 0 5px;
  }
</style>
</head>
<body>

<section class="card card--back" aria-label="Business card, contact side">
  <svg class="card__bands" viewBox="0 0 540 309" aria-hidden="true">
    <path d="M0,0 H540 V34 Q300,14 0,0 Z" fill="var(--brand-blue)"/>
    <path d="M0,3 Q300,22 540,44" fill="none" stroke="var(--brand-red)" stroke-width="4"/>
    <path d="M0,236 Q160,292 540,296 V309 H0 Z" fill="var(--brand-blue)"/>
    <path d="M0,226 Q160,283 540,286" fill="none" stroke="var(--brand-red)" stroke-width="4"/>
  </svg>

  <div class="wordmark">
    <span class="wordmark__dot"></span>
    <span>
      <span class="wordmark__name wordmark__name--main">Blue Harbor</span>
      <span class="wordmark__name wordmark__name--sub">Trophies &amp; Awards</span>
    </span>
  </div>

  <ul class="contact-list">
    <li class="contact-list__item">
      <svg class="contact-list__icon" viewBox="0 0 14 14" aria-hidden="true"><rect width="14" height="14" rx="2" fill="var(--brand-red)"/><path d="M4 3h2l1 2.5-1.2 1a6 6 0 0 0 2.7 2.7l1-1.2L12 9v2a1 1 0 0 1-1 1A8 8 0 0 1 3 4a1 1 0 0 1 1-1z" fill="#fff"/></svg>
      <span>555-555-2190</span>
    </li>
    <li class="contact-list__item">
      <svg class="contact-list__icon" viewBox="0 0 14 14" aria-hidden="true"><rect width="14" height="14" rx="2" fill="var(--brand-red)"/><rect x="3" y="6" width="8" height="5" fill="#fff"/><rect x="4.5" y="3" width="5" height="3" fill="#fff"/></svg>
      <span>555-555-2186</span>
    </li>
    <li class="contact-list__item">
      <svg class="contact-list__icon" viewBox="0 0 14 14" aria-hidden="true"><rect width="14" height="14" rx="2" fill="var(--brand-red)"/><rect x="3" y="4" width="8" height="6" fill="#fff"/><path d="M3 4l4 3.5L11 4" fill="none" stroke="var(--brand-red)" stroke-width="1"/></svg>
      <span>blueharbor@blueharbortrophyco.example</span>
    </li>
    <li class="contact-list__item">
      <svg class="contact-list__icon" viewBox="0 0 14 14" aria-hidden="true"><rect width="14" height="14" rx="2" fill="var(--brand-red)"/><circle cx="7" cy="7" r="4" fill="none" stroke="#fff" stroke-width="1.2"/><path d="M3 7h8M7 3v8" stroke="#fff" stroke-width="1"/></svg>
      <span>www.blueharbortrophyco.example</span>
    </li>
    <li class="contact-list__item">
      <svg class="contact-list__icon" viewBox="0 0 14 14" aria-hidden="true"><rect width="14" height="14" rx="2" fill="var(--brand-red)"/><path d="M7 2.5a3 3 0 0 1 3 3c0 2.2-3 6-3 6s-3-3.8-3-6a3 3 0 0 1 3-3z" fill="#fff"/><circle cx="7" cy="5.5" r="1" fill="var(--brand-red)"/></svg>
      <span>415 W 9th Ave, Millbrook, Ky 70384</span>
    </li>
  </ul>

  <div class="owner">
    <p class="owner__name"><span class="owner__first">Dale</span> Penrow</p>
    <p class="owner__title">Owner</p>
  </div>
</section>

<section class="card card--front" aria-label="Business card, product side">
  <svg class="card__bands" viewBox="0 0 540 309" aria-hidden="true">
    <path d="M0,0 H540 V42 Q240,16 0,0 Z" fill="var(--brand-blue)"/>
    <path d="M0,3 Q240,24 540,52" fill="none" stroke="var(--brand-red)" stroke-width="4"/>
    <path d="M0,250 Q300,268 540,300 V309 H0 Z" fill="var(--brand-blue)"/>
    <path d="M0,240 Q300,258 540,291" fill="none" stroke="var(--brand-red)" stroke-width="4"/>
  </svg>

  <div class="wordmark">
    <span class="wordmark__dot"></span>
    <span>
      <span class="wordmark__name wordmark__name--main">Blue Harbor</span>
      <span class="wordmark__name wordmark__name--sub">Trophies &amp; Awards</span>
    </span>
  </div>

  <div class="products">
    <p class="products__label">Our Products:</p>
    <ul class="products__list">
      <li class="products__item">Trophies</li>
      <li class="products__item">Plaques</li>
      <li class="products__item">Name Plates</li>
      <li class="products__item">Name Tags</li>
      <li class="products__item">Desk Sets</li>
      <li class="products__item">Medals</li>
      <li class="products__item">Certificates...</li>
    </ul>
  </div>
</section>

</body>
</html>
```